Letterhead Design Project

Attached is our new Logo and a copy of our old letter head
Looking to rebrand with our new logo

Reason: I want to show a business card design

Industry/Entity Type

Film Production

Colors

Designer to choose colors to be used in the design.

Requirements
Must have
• The information on the old letterhead

```html
<!DOCTYPE html>
<html lang="en">
<head>
<meta charset="utf-8">
<title>Corvane International Letterhead</title>
<link rel="stylesheet" href="https://fonts.googleapis.com/css2?family=Source+Sans+3:wght@400;600;700&display=swap">
<style>
  :root {
    --brand-blue: #1f64a6;
    --brand-orange: #f07f1f;
    --paper: #ffffff;
    --text-white: #ffffff;
  }
  html, body {
    margin: 0;
    padding: 0;
    width: 809px;
    height: 1200px;
    overflow: hidden;
    background: var(--paper);
  }
  .letterhead {
    position: relative;
    width: 809px;
    height: 1200px;
    background: var(--paper);
    font-family: "Source Sans 3", sans-serif;
    color: var(--brand-blue);
  }
  .brand {
    position: absolute;
    left: 52px;
    top: 92px;
    width: 180px;
  }
  .brand-mark {
    display: block;
    width: 22px;
    height: 22px;
    border-radius: 50%;
    background: var(--brand-orange);
    margin-bottom: 8px;
  }
  .brand-name {
    margin: 0;
    font-size: 26px;
    font-weight: 700;
    line-height: 1.05;
    color: var(--brand-blue);
  }
  .header-rule {
    position: absolute;
    left: 240px;
    top: 88px;
    width: 3px;
    height: 100px;
    background: var(--brand-orange);
  }
  .header-info {
    position: absolute;
    left: 258px;
    top: 104px;
    white-space: nowrap;
  }
  .tagline {
    margin: 0 0 8px;
    font-size: 19px;
    font-weight: 600;
    color: var(--brand-blue);
  }
  .contact {
    display: flex;
    align-items: center;
    gap: 16px;
    font-size: 16px;
    font-weight: 600;
    color: var(--brand-orange);
  }
  .contact-item {
    display: flex;
    align-items: center;
    gap: 5px;
  }
  .contact-item svg { width: 15px; height: 15px; }
  .addresses {
    position: absolute;
    left: 0;
    right: 0;
    top: 1052px;
    margin: 0;
    text-align: center;
    font-size: 18px;
    font-weight: 600;
    color: var(--brand-blue);
    white-space: nowrap;
  }
  .addresses .divider { margin: 0 18px; }
  .footer-band {
    position: absolute;
    left: 0;
    right: 0;
    bottom: 0;
    height: 100px;
    background: var(--brand-orange);
    color: var(--text-white);
    text-align: center;
    padding-top: 14px;
    box-sizing: border-box;
  }
  .divisions {
    margin: 0;
    font-size: 15px;
    font-weight: 600;
    white-space: nowrap;
  }
  .legal {
    margin: 4px 0 0;
    font-size: 12px;
    line-height: 1.35;
  }
</style>
</head>
<body>
<div class="letterhead">
  <div class="brand">
    <span class="brand-mark"></span>
    <p class="brand-name">Corvane International</p>
  </div>

  <div class="header-rule"></div>

  <div class="header-info">
    <p class="tagline">Supply &amp; Management of Infrastructure &amp; Logistics</p>
    <div class="contact">
      <span class="contact-item">
        <svg viewBox="0 0 24 24" aria-hidden="true"><path fill="currentColor" d="M6.6 10.8a15.1 15.1 0 0 0 6.6 6.6l2.2-2.2c.3-.3.7-.4 1-.2 1.1.4 2.3.6 3.6.6.6 0 1 .4 1 1V20c0 .6-.4 1-1 1A17 17 0 0 1 3 4c0-.6.4-1 1-1h3.5c.6 0 1 .4 1 1 0 1.3.2 2.5.6 3.6.1.3 0 .7-.2 1z"/></svg>
        0400 123 456
      </span>
      <span class="contact-item">@ hello@corvane.com.au</span>
    </div>
  </div>

  <p class="addresses">P.O. Box 512 Eastvale QLD 4300<span class="divider">|</span>P.O. Box 318 Westmere NSW 2171</p>

  <footer class="footer-band">
    <p class="divisions">&#9830; Corvane Film Services &#9830; Corvane Pilot Escorts &#9830; Corvane Tour Management &#9830; Corvane Driver</p>
    <p class="legal">are divisions of Corvane International Pty Ltd<br>ACN 000 000 000 &nbsp;ABN 00 000 000 000</p>
  </footer>
</div>
</body>
</html>
```